LITTLE DESIGN WORK REQUIRED!

UPDATE: WE WEREN'T OVERLY ECSTATIC WITH THE DESIGNS WE WERE RECEIVING SO WE DID MOST OF THE DESIGN WORK OURSELVES...

PLEASE SEE THE NEWLY ATTACHED PPT DOC TO VIEW NEARLY EXACT REPLICAS OF WHAT WE WANT THE SITE TO LOOK LIKE. WE NOW NEED YOUR HELP TO MAKE IT LOOK LIKE SOMETHING WORTHY OF THE WEB.

NO CODING REQUIRED - EXPECTED OUTPUT PSD FILES

Hi everyone!

We're looking for a designer to work their magic for our site! We're a not-for-profit program aimed at helping young people realise their potential!

In the attached PPT file, you'll notice we've already DESIGNED THE ENTIRE SITE IN POWERPOINT. Now, we need YOU to make the small changes we requested in the document as well as design the whole thing in psd.

Any questions, don't hesitate to ask.

Brook-Rise
Updates

We've done about 95% of the design for you. Please fine-tune it. See the newly attached PPT doc for details. 

The best two designs will win. This project closes on Friday - please message us if you are absolutely sure you cannot make the deadline.

Thanks,
Brook-Rise

```html
<!DOCTYPE html>
<html lang="en">
<head>
<meta charset="utf-8">
<title>Brook-Rise</title>
<link rel="stylesheet" href="https://fonts.googleapis.com/css2?family=Montserrat:wght@700;800&family=Titillium+Web:ital,wght@0,400;0,600;0,700;1,400;1,600&display=swap">
<style>
:root{
  --green:#8ccc00;
  --green-nav:#6aa300;
  --green-bar:#7ab83f;
  --green-foot:#6fa600;
  --green-foot-link:#4d8500;
  --blue-bar:#3a9fde;
  --friend-blue:#3b5998;
  --ink:#2b2b2b;
  --grey:#8a8a8a;
  --grey-light:#d9d9d9;
  --body:#444;
  --white:#fff;
}
*{margin:0;padding:0;box-sizing:border-box}
html,body{width:900px;height:1200px;overflow:hidden;background:var(--white)}
body{position:relative;font-family:"Titillium Web",Arial,sans-serif;color:var(--body)}
.abs{position:absolute}

/* header */
.brand{left:150px;top:58px;display:flex;align-items:center;gap:8px}
.brand-dot{width:26px;height:26px;border-radius:50%;background:var(--green)}
.brand-name{font-family:"Titillium Web",sans-serif;font-weight:700;font-size:24px;color:var(--ink);letter-spacing:.5px}
.quote{left:621px;top:27px;font-style:italic;font-weight:600;font-size:9px;line-height:11px;color:var(--grey)}
.quote-author{left:626px;top:48px;font-size:12px;color:var(--grey)}
.share{left:699px;top:53px;width:40px;height:14px;background:var(--friend-blue);color:#fff;font-size:8px;font-weight:700;text-align:center;line-height:14px}
.nav{left:150px;top:84px;width:590px;height:22px;border-bottom:1px solid var(--grey-light);font-weight:700;font-size:11px;color:var(--green-nav)}
.nav span{position:absolute;top:0}
.nav .active{color:#111}
.hero{left:150px;top:119px;width:589px;height:154px;background:var(--green)}
.hero-title{left:167px;top:139px;font-family:Montserrat,sans-serif;font-weight:800;font-size:25px;line-height:30.5px;color:var(--white);letter-spacing:1.2px}
.hero-photo{left:453px;top:119px;width:286px;height:154px;background:linear-gradient(180deg,#3b6fb3 0%,#8fb3dd 30%,#5a6d9a 48%,#35507d 60%,#6d8a3a 72%,#9aa83c 100%)}
.welcome{left:150px;top:285px;font-weight:700;font-size:13px;color:var(--ink)}
.intro{left:150px;top:300px;width:590px;font-size:11.5px;line-height:13px;color:var(--grey);text-transform:uppercase}
.intro b{color:#666}
.btn{background:linear-gradient(#f6f6f6,#e1e1e1);border:1px solid #d6d6d6;border-radius:2px;font-size:8px;color:#777;text-align:center}
.learn{left:670px;top:324px;width:70px;height:18px;line-height:16px}
.rule{left:150px;top:352px;width:590px;height:1px;background:#cfcfcf}

/* posts */
.bar{left:150px;width:416px;height:21px;color:#fff;font-size:12px;line-height:21px;padding-left:10px}
.bar.blue{background:var(--blue-bar);top:375px}
.bar.green{background:var(--green-bar);top:632px}
.thumb{width:122px;height:80px}
.t-grass{background:linear-gradient(160deg,#5d7a45,#b7a07f 45,#6aa53a)}
.t-sky{background:radial-gradient(circle at 50% 70%,#dbe9ff 0,#5b8fe0 30%,#1a3f9a 75%)}
.t-office{background:linear-gradient(120deg,#e8ecf0,#b9c4cc 50,#2b2b2b 70,#e6e6e6)}
.post-title{font-size:12px;color:#333}
.date{font-style:italic;font-size:7.5px;color:#555;display:flex;align-items:center;gap:6px}
.date i{display:block;width:8px;height:8px;border:1px solid #aaa}
.excerpt{width:125px;font-size:7.5px;line-height:11px;color:#333}
.stripe{left:150px;width:416px;height:5px;background:repeating-linear-gradient(135deg,#e4e4e4 0 2px,#f6f6f6 2px 4px)}
.pager{left:247px;top:919px;display:flex;gap:5px}
.pager span{width:16px;height:15px;border:1px solid #ddd;font-size:7px;line-height:13px;text-align:center;color:#999}
.pager .cur{color:#333}
.pager .next{width:40px;background:#7d7d7d;color:#fff;border-color:#777;border-radius:2px}

/* sidebar */
.side-line{left:598px;top:368px;width:1px;height:592px;background:#ececec}
.side-h{left:617px;font-size:11px;color:#444}
.widget{left:617px;top:392px;width:120px;height:128px;border:1px solid #c8cfe0}
.widget-head{height:13px;background:var(--friend-blue);color:#fff;font-size:5px;line-height:13px;padding:0 3px;display:flex;justify-content:space-between}
.widget-head b{font-size:6px}
.w-item{display:flex;gap:4px;padding:3px 3px 0}
.w-item i{width:9px;height:9px;background:#4d6aa6;flex:none}
.w-item p{font-size:4.5px;line-height:5.6px;color:#3b5998;font-weight:700}
.w-item p span{display:block;color:#999;font-weight:400}
.widget-foot{position:absolute;left:3px;bottom:2px;font-size:4px;color:#777}
.side-rule{left:617px;width:123px;height:1px;background:#e6e6e6}
.pop{left:617px;display:flex;gap:10px}
.pop i{width:36px;height:28px;display:block;flex:none}
.pop p{font-size:7.5px;line-height:10px;color:#333;width:75px}
.pop p span{display:block;color:#999;font-size:7px}
.learn-side{left:676px;top:742px;width:57px;height:15px;line-height:13px}
.portrait{left:618px;top:803px;width:84px;height:94px;background:linear-gradient(180deg,#2c5fa8,#1b3f7a 55%,#5a6c80)}
.name{left:620px;top:907px;font-weight:700;font-size:11px;color:#333}
.role{left:620px;top:921px;font-size:7px;line-height:11px;color:#333}

/* footer */
.tweets{left:113px;top:978px;width:666px;height:62px;background:linear-gradient(#fff,#f1f1f1)}
.bird{left:119px;top:997px;width:26px;height:20px;border-radius:50%;background:#444}
.tweet-text{left:160px;top:995px;width:440px;font-size:9.5px;line-height:12px;color:#888}
.tweet-text a{color:#2a8bd0}
.all{left:663px;top:1001px;width:58px;height:18px;line-height:16px}
.foot{left:113px;top:1040px;width:666px;height:142px;background:var(--green-foot)}
.col{top:1059px;width:108px}
.col h3{font-weight:400;font-size:10px;color:#fff;margin-bottom:6px}
.col a{display:block;font-size:7px;color:var(--green-foot-link);height:20px;line-height:14px;border-bottom:1px dotted #82b626;text-decoration:none}
.col a.hover{color:#e8ffd0;padding-left:6px}
</style>
</head>
<body>

<header>
  <div class="abs brand"><span class="brand-dot"></span><span class="brand-name">Brook-Rise</span></div>
  <p class="abs quote">What would you do if you knew<br>you could not fail?</p>
  <p class="abs quote-author">- R. Hallward</p>
  <div class="abs share">Share</div>
  <nav class="abs nav">
    <span class="active" style="left:179px">HOME</span>
    <span style="left:250px">RESOURCES</span>
    <span style="left:348px">WORKSHOPS</span>
    <span style="left:444px">AMBASSADORS</span>
    <span style="left:560px">FEATS</span>
  </nav>
</header>

<section>
  <div class="abs hero"></div>
  <h1 class="abs hero-title">CHALLANGES<br>THAT DARE YOU<br>TO PUSH<br>YOURSELF</h1>
  <div class="abs hero-photo" role="img" aria-label="Snow-capped mountain over savanna with elephants walking"></div>
  <h2 class="abs welcome">WELCOME TO BROOK-RISE</h2>
  <p class="abs intro"><b>Brook-Rise</b> is a not-for-profit program aimed at helping people – especially young people – set and achieve authentic, meaningful, and audacious goals.</p>
  <div class="abs btn learn">LEARN MORE &rsaquo;</div>
  <div class="abs rule"></div>
</section>

<main>
  <div class="abs bar blue">RECENT POSTS</div>
  <div class="abs thumb t-grass" style="left:150px;top:412px" role="img" aria-label="Students working on laptops on the grass"></div>
  <div class="abs thumb t-sky" style="left:298px;top:412px" role="img" aria-label="Silhouette of a climber with arms raised on a summit"></div>
  <div class="abs thumb t-grass" style="left:442px;top:412px" role="img" aria-label="Students working on laptops on the grass"></div>
  <p class="abs post-title" style="left:149px;top:499px">Title</p>
  <p class="abs date" style="left:150px;top:524px"><i></i>April 2012</p>
  <p class="abs date" style="left:298px;top:524px"><i></i>April 2012</p>
  <p class="abs date" style="left:443px;top:524px"><i></i>April 2012</p>
  <p class="abs excerpt" style="left:150px;top:543px">Lorem ipsum dolor sit amet, consectetur adipiscing elit. Aenean nisl orci, condimentum ultrices consequat eu, vehicula ac mauris. Ut adipiscing, leo nec.</p>
  <p class="abs excerpt" style="left:298px;top:543px">Lorem ipsum dolor sit amet, consectetur adipiscing elit. Aenean nisl orci, condimentum ultrices consequat eu, vehicula ac mauris. Ut adipiscing, leo nec.</p>
  <p class="abs excerpt" style="left:443px;top:543px">Lorem ipsum dolor sit amet, consectetur adipiscing elit. Aenean nisl orci, condimentum ultrices consequat eu, vehicula ac mauris. Ut adipiscing, leo nec.</p>
  <div class="abs stripe" style="top:612px"></div>

  <div class="abs bar green">RECENT POSTS</div>
  <div class="abs thumb t-office" style="left:150px;top:674px" role="img" aria-label="Businesswoman in a meeting room with colleagues"></div>
  <div class="abs thumb t-sky" style="left:298px;top:674px" role="img" aria-label="Silhouette of a climber with arms raised on a summit"></div>
  <div class="abs thumb t-office" style="left:440px;top:674px" role="img" aria-label="Businesswoman in a meeting room with colleagues"></div>
  <p class="abs post-title" style="left:149px;top:765px">Title</p>
  <p class="abs date" style="left:150px;top:790px"><i></i>April 2012</p>
  <p class="abs date" style="left:298px;top:790px"><i></i>April 2012</p>
  <p class="abs date" style="left:443px;top:790px"><i></i>April 2012</p>
  <p class="abs excerpt" style="left:150px;top:802px">Lorem ipsum dolor sit amet, consectetur adipiscing elit. Aenean nisl orci, condimentum ultrices consequat eu, vehicula ac mauris. Ut adipiscing, leo nec.</p>
  <p class="abs excerpt" style="left:298px;top:802px">Lorem ipsum dolor sit amet, consectetur adipiscing elit. Aenean nisl orci, condimentum ultrices consequat eu, vehicula ac mauris. Ut adipiscing, leo nec.</p>
  <p class="abs excerpt" style="left:443px;top:802px">Lorem ipsum dolor sit amet, consectetur adipiscing elit. Aenean nisl orci, condimentum ultrices consequat eu, vehicula ac mauris. Ut adipiscing, leo nec.</p>
  <div class="abs stripe" style="top:873px"></div>

  <div class="abs pager">
    <span>&lsaquo;</span><span>1</span><span class="cur">2</span><span>3</span><span>4</span><span>5</span><span>6</span><span class="next">Next &rsaquo;</span>
  </div>
</main>

<aside>
  <div class="abs side-line"></div>
  <h3 class="abs side-h" style="top:368px">Stay in touch</h3>
  <div class="abs widget">
    <div class="widget-head"><span>Recent Activity</span><b>Friendbook</b></div>
    <div class="w-item"><i></i><p>Calling all makers, come back soon<span>1,801 people shared this.</span></p></div>
    <div class="w-item"><i></i><p>Platform update: new developer site<span>1,866 people shared this.</span></p></div>
    <div class="w-item"><i></i><p>Application roles and security<span>1,200 people shared this.</span></p></div>
    <div class="w-item"><i></i><p>The next step for credits<span>3,383 people shared this.</span></p></div>
    <div class="w-item"><i></i><p>Web games kit 0.1<span>752 people shared this.</span></p></div>
    <span class="widget-foot">Social plugin</span>
  </div>
  <div class="abs side-rule" style="top:544px"></div>
  <h3 class="abs side-h" style="top:555px">Most Popular Posts</h3>
  <div class="abs pop" style="top:581px"><i style="background:linear-gradient(135deg,#f15a24,#fff 50%,#f15a24)" role="img" aria-label="Orange abstract post thumbnail"></i><p>Maecenas metus nulla, facili sis in bibendum a, pretium<span>28 October 2010</span></p></div>
  <div class="abs side-rule" style="top:624px"></div>
  <div class="abs pop" style="top:631px"><i style="background:linear-gradient(135deg,#c8102e,#333)" role="img" aria-label="Group photo post thumbnail"></i><p>Maecenas metus nulla, facili sis in bibendum a, pretium<span>28 October 2010</span></p></div>
  <div class="abs side-rule" style="top:674px"></div>
  <div class="abs pop" style="top:683px"><i style="background:linear-gradient(135deg,#9fc7d6,#6b8a99)" role="img" aria-label="Portrait post thumbnail"></i><p>Maecenas metus nulla, facili sis in bibendum a, pretium<span>28 October 2010</span></p></div>
  <div class="abs btn learn-side">Learn more</div>
  <div class="abs side-rule" style="top:772px"></div>
  <h3 class="abs side-h" style="top:779px">Get to know us</h3>
  <div class="abs portrait" role="img" aria-label="Portrait of a young entrepreneur in a grey shirt"></div>
  <p class="abs name">John Doe</p>
  <p class="abs role">Young entrepreneur &amp;<br>Brook-Rise Ambassador</p>
</aside>

<footer>
  <div class="abs tweets"></div>
  <div class="abs bird"></div>
  <p class="abs tweet-text">Lorem ipsum dolor site amet, consectetur adipiscining lei. Aenean nisl orci, condimentum ultrictu siploatus sit colectus @<a>simpla</a> @<a>guy</a> ! – 9:11 AM yesterday – @ <a>how you feel</a></p>
  <div class="abs btn all">All tweets</div>
  <div class="abs foot"></div>
  <div class="abs col" style="left:151px"><h3>Lorem Ipsum</h3><a>Lorem ipsum dolor sit am</a><a>Fringilla vel aliquet</a><a class="hover">&rsaquo; Nec vulputate eget</a><a>Sociis natoque penatibus</a></div>
  <div class="abs col" style="left:270px"><h3>Ipsum</h3><a>Lorem ipsum</a><a>Fringilla vel aliquet</a><a>Nec vulputate eget</a><a>Sociis natoque penatibus</a></div>
  <div class="abs col" style="left:390px"><h3>Fringilla</h3><a>Lorem ipsum dolor</a><a>Fringilla vel aliquet sirius</a><a>Nec vulputate eget</a><a>Sociis</a><a>Nec vulputate eget</a></div>
  <div class="abs col" style="left:509px"><h3>Sitcum Sato</h3><a>Lorem</a><a>Fringilla vel aliquet</a><a>Nec vulputate eget</a><a>Sociis natoque penatibus</a></div>
  <div class="abs col" style="left:628px"><h3>Sirius Sopus</h3><a>Lorem ipsum dolor sit am</a><a>Fringilla vel aliquet</a><a>Nec vulputate eget</a></div>
</footer>

</body>
</html>
```